Korvel Online Guild - Original design for WordPress

The requirement is to develop a custom Wordpress theme.
The content and structure section of the brief is provided as a guide for what visual elements need to be addressed in the theme.
Project is to create an original website design and deliver as a WordPress theme to the client.
About the client
KOG is a not-for-profit organisation founded in 1995 to support and represent the interests of the internet community in Western Australia.
Project Vision
We are looking for a clean and modern web design that befits our technical organisation and members.
Members of the public should be able to visit our website and quickly and easily find what they're looking for - so there is an emphasis on readability.
Given our technical audience, we expect a large number of page views will come from mobile devices - so a responsive layout is essential.
Update May 21 Budget has been added to this project for Coding.
Industry/Entity Type
Internet
Coding
Coded - Design and coding required
Number of Pages Required
3 page
Font styles to use
Requirements
Must have
- A detailed brief is provided which is essential reading and should answer any questions.
- Social Media Accounts: Apologies for the poor wording on this requirement, we'd like icon graphics for Chatterly and Blipster styled appropriately somewhere on the main page.
- We want the best possible outcome, and are keen to discuss any suggestions or clarifications you may have through this process.
Nice to have
- We would prefer backgrounds with a light coloured background, as this gives the site a more modern aesthetic.
- Pictures of Australia are great, but we're primarily based in Perth, Western Australia - so photos of there are much more appropriate for us than Sydney.

```html
<!DOCTYPE html>
<html lang="en">
<head>
<meta charset="utf-8">
<title>Korvel Online Guild</title>
<link href="https://fonts.googleapis.com/css2?family=Open+Sans:wght@300;400;600;700&display=swap" rel="stylesheet">
<style>
:root{
  --green:#0b5c37;
  --green-dark:#084a2c;
  --green-mid:#0a5533;
  --orange:#e6892a;
  --ink:#2b2b2b;
  --body:#666;
  --footer:#3a3a3a;
  --footer-deep:#2e2e2e;
  --panel:#efefef;
  --line:#d8d8d8;
  --icon:#5a5a5a;
}
*{margin:0;padding:0;box-sizing:border-box}
html,body{width:1200px;height:2187px;overflow:hidden}
body{font-family:"Open Sans",Arial,sans-serif;background:#fff;color:var(--body);position:relative}
.abs{position:absolute}

/* hero */
.hero{left:0;top:0;width:1200px;height:535px;background:linear-gradient(180deg,#1c1d24 0%,#3a2e2a 45%,#5a3a22 70%,#1a1c22 100%)}
.hero-skyline{left:0;top:120px;width:1200px;height:415px;background:linear-gradient(180deg,rgba(90,70,50,0) 0%,rgba(120,80,40,.55) 55%,rgba(20,25,35,.9) 85%,#14161c 100%)}
.nav{top:31px;left:376px;display:flex;font-size:11px;color:#fff;text-transform:uppercase}
.nav a{color:#fff;text-decoration:none;margin-right:48px}
.brand{left:105px;top:8px;width:200px;height:200px;border-radius:50%;background:var(--green);border:4px solid #fff;display:flex;align-items:center;justify-content:center;color:#fff;font-weight:700;font-size:46px}
.hero-title{top:228px;width:1200px;text-align:center;color:#fff;font-size:30px;font-weight:700;text-transform:uppercase}
.hero-sub{top:266px;width:1200px;text-align:center;color:#fff;font-size:29px;font-weight:300;text-transform:uppercase}
.hero-btn{left:506px;top:320px;width:179px;height:46px;background:var(--orange);color:#fff;font-size:14px;font-weight:700;text-transform:uppercase;display:flex;align-items:center;justify-content:center}
.arrow{top:280px;width:28px;height:28px;border-radius:50%;background:rgba(255,255,255,.25)}

/* features */
.features{left:99px;top:459px;width:1002px;height:145px;display:flex;box-shadow:0 22px 22px -10px rgba(0,0,0,.35)}
.feature{flex:1;padding:24px 20px 0 85px;color:#fff;position:relative}
.feature:nth-child(1){background:var(--green-dark)}
.feature:nth-child(2){background:var(--green-mid)}
.feature:nth-child(3){background:var(--green)}
.feature h3{font-size:16px;font-weight:700;text-transform:uppercase;margin-bottom:8px}
.feature p{font-size:11px;line-height:22px}
.feature svg{position:absolute;left:26px;top:24px}

/* welcome */
.center{width:1200px;text-align:center}
.sec-title{font-size:20px;font-weight:700;color:var(--ink);text-transform:uppercase}
.sec-sub{font-size:20px;font-weight:400;color:#444;text-transform:uppercase}
.lead{left:200px;width:800px;text-align:center;font-size:12px;line-height:25px}

/* posts */
.post{width:318px}
.post-img{width:318px;height:202px}
.post h4{font-size:13px;font-weight:700;color:var(--ink);text-transform:uppercase;line-height:23px;margin-top:12px;width:275px}
.post-over{padding:40px 26px 0;color:#fff;font-size:11px;line-height:22px;background:linear-gradient(135deg,#0d4f31,#0a3d26)}

/* about */
.about h2{font-size:21px;font-weight:700;color:var(--ink);text-transform:uppercase}
.about p{font-size:11px;line-height:22px;margin-top:14px;width:400px}
.btn-green{display:inline-flex;width:130px;height:38px;background:var(--green);color:#fff;font-size:12px;align-items:center;justify-content:center;border-radius:2px;margin-top:20px}

.widget{background:var(--panel);border:1px solid var(--line)}
.tw-head{height:50px;border-bottom:1px solid var(--line);display:flex;align-items:center;padding-left:20px;font-size:15px;font-weight:600;color:var(--ink);text-transform:uppercase;gap:8px;margin-bottom:16px}
.tweet{display:flex;gap:10px;padding:0 20px;height:60px}
.avatar{width:34px;height:34px;flex:none}
.tweet b{display:block;font-size:10px;color:#444;line-height:12px;width:170px}
.tweet small{display:block;font-size:7.5px;color:#999;margin-top:3px}
.fb{background:#fff;margin:6px;border:1px solid #e3e3e3;height:300px;padding:8px}
.fb-grid{display:grid;grid-template-columns:repeat(5,40px);gap:5px;margin-top:8px}
.fb-grid span{width:40px;height:40px}

/* footer */
.footer{left:0;top:1931px;width:1200px;height:207px;background:var(--footer);color:#bbb}
.footer h5{font-size:13px;font-weight:700;color:#fff;text-transform:uppercase;margin-bottom:14px}
.footer p,.footer li{font-size:11px;line-height:22px;list-style:none}
.footer b{color:#fff}
.bottom{left:0;top:2138px;width:1200px;height:49px;background:var(--footer-deep);color:#bbb;font-size:11px}
.social{left:600px;top:0;height:49px;display:flex;align-items:center;gap:14px}
.social-item{display:flex;align-items:center;gap:5px;color:#ddd;font-size:10px}
.social-item i{width:18px;height:18px;border-radius:50%;background:var(--icon);display:block}
</style>
</head>
<body>

<section class="abs hero" role="img" aria-label="Night skyline of Perth city towers reflected over the river"></section>
<div class="abs hero-skyline"></div>
<div class="abs brand">KOG</div>
<nav class="abs nav"><a>News</a><a>Events</a><a>About Us</a><a>Membership</a><a>Resources</a><a>Media</a><a>Contatc Us</a></nav>
<h1 class="abs hero-title">KOG is a not-for-profit organisation</h1>
<div class="abs hero-sub">Founded in 1995</div>
<div class="abs hero-btn">View our story</div>
<span class="abs arrow" style="left:36px"></span>
<span class="abs arrow" style="left:1127px"></span>

<div class="abs features">
  <div class="feature">
    <svg width="36" height="32" viewBox="0 0 36 32" fill="none" stroke="#fff" stroke-width="3"><rect x="3" y="6" width="22" height="22" rx="4"/><path d="M14 20l2-6L30 2l4 4-14 12z" fill="#fff"/></svg>
    <h3>Members Portal</h3><p>Lorem Ipsum is simply dummy text of the printing and typesetting industry Lorem Ipsum is simply dummy...</p>
  </div>
  <div class="feature">
    <svg width="60" height="40" viewBox="0 0 60 40" fill="#fff" style="left:14px"><path d="M2 8l14-4 10 6 8-4 14 2 10 10-6 4-10-8-10 6 14 10-4 4-4-2-4 4-4-2-4 2-16-14-8-2z"/></svg>
    <h3>Member Benefits</h3><p>Lorem Ipsum is simply dummy text of the printing and typesetting industry. Lorem Ipsum has been the industry's...</p>
  </div>
  <div class="feature">
    <svg width="38" height="38" viewBox="0 0 38 38" fill="none" stroke="#fff" stroke-width="5"><path d="M6 16a13 13 0 0 1 24-5M32 22a13 13 0 0 1-24 5"/><path d="M32 3v10H22M6 35V25h10" stroke-width="4"/></svg>
    <h3>Resources</h3><p>Lorem Ipsum is simply dummy text of the printing and typesetting industry. Lorem Ipsum has been the industry's...</p>
  </div>
</div>

<h2 class="abs center sec-title" style="top:660px">Welcome to KOG</h2>
<div class="abs center sec-sub" style="top:694px">Korvel Online Guild</div>
<p class="abs lead" style="top:730px">The Korvel Online Guild (Inc.) is an organisation that was formed in 1995 to represent the Internet community in Western Australia. At the time of formation, pending regulation and uncertainty meant that collaboration between different businesses in the Internet industry was a necessity.</p>

<h2 class="abs center sec-title" style="top:848px">Recent Posts</h2>
<p class="abs center" style="top:884px;font-size:12px">Lorem Ipsum is simply dummy text of the printing and typesetting industry. Lorem Ipsum has been the industry's standard dummy text ever since</p>

<article class="abs post" style="left:99px;top:945px">
  <div class="post-img post-over">The Mandatory Data Retention Bill has been the topic of many conversations in our industry over the past months, with the Bill being passed by both houses of Parliament on 26 March 2015...<br><i>by marla on Wed, 29/04/2015 - 10:47am</i></div>
  <h4>Request for member submissions on data retention FAQ</h4>
</article>
<article class="abs post" style="left:441px;top:945px">
  <div class="post-img" role="img" aria-label="Figure standing in a corridor of server racks under a cloudy sky" style="background:linear-gradient(180deg,#2a6a8e,#9cc8dc 50%,#3a4a55)"></div>
  <h4>Request for member submissions on data retention FAQ</h4>
</article>
<article class="abs post" style="left:783px;top:945px">
  <div class="post-img" role="img" aria-label="Technician working on a server rack with a laptop" style="background:linear-gradient(135deg,#5a6e86,#c8d2dc 60%,#e8ecf0)"></div>
  <h4>Request for member submissions on data retention FAQ</h4>
</article>
<article class="abs post" style="left:99px;top:1237px">
  <div class="post-img" role="img" aria-label="Close view of lit network switches in a rack" style="background:linear-gradient(135deg,#1c2a40,#3c5a7a 60%,#152030)"></div>
  <h4>Request for member submissions on data retention FAQ</h4>
</article>
<article class="abs post" style="left:441px;top:1237px">
  <div class="post-img" role="img" aria-label="Hands typing on a laptop keyboard beside a coffee cup" style="background:linear-gradient(135deg,#2e5a6e,#8ab0bc 55%,#d4dde0)"></div>
  <h4>Request for member submissions on data retention FAQ</h4>
</article>
<article class="abs post" style="left:783px;top:1237px">
  <div class="post-img" role="img" aria-label="Business team behind a handshake" style="background:linear-gradient(180deg,#8a8a8a,#3a3a3a 70%,#1e1e1e)"></div>
  <h4>Request for member submissions on data retention FAQ</h4>
</article>

<section class="abs about" style="left:99px;top:1577px">
  <h2>About KOG</h2>
  <p>The Korvel Online Guild (Inc.) is an organisation that was formed in 1995 to represent the Internet community in Western Australia. At the time of formation, pending regulation and uncertainty meant that collaboration between different businesses in the Internet industry was a necessity.</p>
  <p style="margin-top:22px">Since then, KOG has helped the industry to continue to grow in WA. Leading many vital debates and helping to set policy at different levels, KOG has been instrumental in providing an innovative range of services to association members.</p>
  <span class="btn-green">Read More Info</span>
</section>

<aside class="abs widget" style="left:554px;top:1555px;width:260px;height:313px">
  <div class="tw-head"><svg width="14" height="14"><circle cx="7" cy="7" r="6" fill="#2aa3dc"/></svg>Blipster</div>
  <div class="tweet"><span class="avatar" role="img" aria-label="Member avatar" style="background:#7a9ab4"></span><div><b>Phasellus molestie magna non est bibendum non venenatis nisl.</b><small>Posted on May 21st &nbsp;|&nbsp; 32 Comments</small></div></div>
  <div class="tweet"><span class="avatar" role="img" aria-label="Member avatar" style="background:#c8b49a"></span><div><b>Phasellus molestie magna non est bibendum non venenatis nisl.</b><small>Posted on May 21st &nbsp;|&nbsp; 32 Comments</small></div></div>
  <div class="tweet"><span class="avatar" role="img" aria-label="Member avatar" style="background:#8a8a8a"></span><div><b>Phasellus molestie magna non est bibendum non venenatis nisl.</b><small>Posted on May 21st &nbsp;|&nbsp; 32 Comments</small></div></div>
  <div class="tweet"><span class="avatar" role="img" aria-label="Member avatar" style="background:#b4806a"></span><div><b>Phasellus molestie magna non est bibendum non venenatis nisl.</b><small>Posted on May 21st &nbsp;|&nbsp; 32 Comments</small></div></div>
</aside>

<aside class="abs widget" style="left:840px;top:1555px;width:261px;height:315px">
  <div class="fb">
    <div style="display:flex;gap:8px;align-items:center">
      <span style="width:40px;height:40px;background:var(--green);border-radius:50%"></span>
      <div><b style="font-size:11px;color:#3b5998">KOG</b><div style="font-size:8px;border:1px solid #ccc;padding:1px 4px;margin-top:3px;color:#3b5998">Нравится</div></div>
    </div>
    <p style="font-size:8.5px;margin-top:12px;color:#555">29 192 пользователям нравится <span style="color:#3b5998">Marketvale</span>.</p>
    <div class="fb-grid" role="img" aria-label="Grid of supporter profile pictures">
      <span style="background:#7a6a5a"></span><span style="background:#b49a7a"></span><span style="background:#5a7a4a"></span><span style="background:#8a6a6a"></span><span style="background:#e8c87a"></span>
      <span style="background:#5ab4b4"></span><span style="background:#e0c060"></span><span style="background:#bbb"></span><span style="background:#c88a3a"></span><span style="background:#999"></span>
      <span style="background:#6a9ab4"></span><span style="background:#dde"></span><span style="background:#e0c040"></span><span style="background:#444"></span><span style="background:#8a3a2a"></span>
      <span style="background:#5ab4b4"></span><span style="background:#d8b060"></span><span style="background:#aaa"></span><span style="background:#c88a3a"></span><span style="background:#777"></span>
    </div>
    <p style="font-size:7.5px;margin-top:10px;border-top:1px solid #e3e3e3;padding-top:4px;color:#777">Социальный плагин Chatterly</p>
  </div>
</aside>

<footer class="abs footer">
  <div class="abs" style="left:99px;top:36px">
    <h5>Welcome</h5>
    <ul style="display:grid;grid-template-columns:128px 80px"><li>Home</li><li>Events</li><li>About KOG</li><li>Resources</li><li>News</li><li>&nbsp;Contact</li><li>Peering Hub</li><li></li><li>Membership</li></ul>
  </div>
  <div class="abs" style="left:347px;top:36px;width:210px">
    <h5>Join Us</h5><p>We are looking to increase our membership base. <b>Click here</b> to find out how you can join.</p>
  </div>
  <div class="abs" style="left:602px;top:36px;width:210px">
    <h5>Our Members</h5><p>KOG currently has three types of membership. Here is a list of our <b>current members.</b></p>
  </div>
  <div class="abs" style="left:890px;top:36px;width:210px">
    <h5>Get in Touch</h5><p>Got a question for us? Would you like to know more? Fill out our <b>contact form</b> and we will be straight in touch.</p>
  </div>
</footer>
<div class="abs bottom">
  <span class="abs" style="left:99px;top:16px">© Copyright 2015 - KOG - All rights reserved</span>
  <div class="abs social">
    <span>Connect with our social network :</span>
    <span class="social-item"><i></i>Chatterly</span>
    <span class="social-item"><i></i>Blipster</span>
    <span class="social-item"><i></i>Plusline</span>
    <span class="social-item"><i></i>Pinvault</span>
    <span class="social-item"><i></i>Proflink</span>
  </div>
</div>

</body>
</html>
```